Business Card for Auto Dealership - Clean, sharp and professional

Please use the maroon logo with the grey background. Need a sharp, clean and professional business card for an Auto Dealer. In the files provides there is three different logos. I have not decided which one to go with yet. Right now I am favoring the grey/silver background. I would like my contact info on there and the website as well. I feel like less is more and want something simple, clean and sharp. Thank you in advance for your tie and effort! I also need email signature, letterhead, etc after this

Target Market(s)

Car buyers

Industry/Entity Type

Automotive

Contact Information for Business Card

Dean
555-417-2386
www.BrinwoodAutoHub.example
Dean@BrinwoodAutoHub.example

Font styles to use
Serif
Sans Serif

Requirements
Must have
• Please use the maroon logo with the grey background. Business Card Details and logo from files. Please stick to the logo colors

```html
<!DOCTYPE html>
<html lang="en">
<head>
<meta charset="utf-8">
<title>Brinwood Auto Hub — Business Card</title>
<link rel="stylesheet" href="https://fonts.googleapis.com/css2?family=Open+Sans:wght@400;700&display=swap">
<style>
  :root {
    --maroon: #4a1515;
    --maroon-ink: #5a1d1d;
    --paper: #ffffff;
    --backdrop: #e4e2e0;
    --card-shadow: rgba(0, 0, 0, 0.18);
  }
  * { box-sizing: border-box; margin: 0; padding: 0; }
  html, body {
    width: 1200px;
    height: 780px;
    overflow: hidden;
  }
  body {
    background: var(--backdrop);
    font-family: "Open Sans", Arial, sans-serif;
    display: flex;
    align-items: center;
    justify-content: center;
    gap: 40px;
  }
  .card {
    width: 530px;
    height: 303px;
    box-shadow: 0 6px 18px var(--card-shadow);
    position: relative;
  }
  .card--front {
    background: var(--maroon);
    display: flex;
    align-items: center;
    justify-content: center;
  }
  .brand-name {
    font-family: "Open Sans", Arial, sans-serif;
    font-weight: 700;
    text-transform: uppercase;
    line-height: 1.05;
    letter-spacing: 0.02em;
  }
  .card--front .brand-name {
    color: var(--paper);
    font-size: 40px;
    text-align: center;
  }
  .card--back {
    background: var(--paper);
    display: flex;
    align-items: center;
    padding: 0 34px 0 40px;
  }
  .card--back .brand-name {
    color: var(--maroon-ink);
    font-size: 25px;
    width: 200px;
  }
  .divider {
    width: 1px;
    height: 104px;
    background: var(--maroon-ink);
    margin: 0 22px 0 18px;
  }
  .contact {
    color: var(--maroon-ink);
  }
  .contact__name {
    font-weight: 700;
    font-size: 17px;
    letter-spacing: 0.04em;
    text-transform: uppercase;
    margin-bottom: 16px;
  }
  .contact__list {
    list-style: none;
    font-size: 13px;
    line-height: 1.5;
  }
  .contact__item {
    display: flex;
    align-items: center;
    gap: 7px;
    white-space: nowrap;
  }
  .contact__icon {
    width: 13px;
    height: 13px;
    flex: none;
  }
</style>
</head>
<body>
  <section class="card card--front" aria-label="Card front">
    <p class="brand-name">Brinwood<br>Auto Hub</p>
  </section>

  <section class="card card--back" aria-label="Card back">
    <p class="brand-name">Brinwood<br>Auto Hub</p>
    <span class="divider"></span>
    <div class="contact">
      <p class="contact__name">Dean</p>
      <ul class="contact__list">
        <li class="contact__item">
          <svg class="contact__icon" viewBox="0 0 14 14" aria-hidden="true">
            <rect width="14" height="14" rx="2" fill="var(--maroon-ink)"/>
            <path d="M4 3.2c.4-.3.9-.2 1.1.2l.7 1.3c.2.4 0 .7-.3 1l-.4.3c.4.9 1.1 1.6 2 2l.3-.4c.3-.3.6-.5 1-.3l1.3.7c.4.2.5.7.2 1.1l-.5.6c-.4.4-1 .5-1.6.3C5.9 9.3 4.7 8.1 3.9 6.2c-.2-.6-.1-1.2.3-1.6z" fill="#fff"/>
          </svg>
          555-417-2386
        </li>
        <li class="contact__item">
          <svg class="contact__icon" viewBox="0 0 14 14" aria-hidden="true">
            <rect width="14" height="14" rx="2" fill="var(--maroon-ink)"/>
            <rect x="2.5" y="4" width="9" height="6" fill="none" stroke="#fff" stroke-width="1"/>
            <path d="M2.5 4l4.5 3.5L11.5 4" fill="none" stroke="#fff" stroke-width="1"/>
          </svg>
          Dean@BrinwoodAutoHub.example
        </li>
        <li class="contact__item">
          <svg class="contact__icon" viewBox="0 0 14 14" aria-hidden="true">
            <rect width="14" height="14" rx="2" fill="var(--maroon-ink)"/>
            <circle cx="7" cy="7" r="4.2" fill="none" stroke="#fff" stroke-width="0.9"/>
            <ellipse cx="7" cy="7" rx="1.8" ry="4.2" fill="none" stroke="#fff" stroke-width="0.8"/>
            <path d="M2.8 7h8.4" stroke="#fff" stroke-width="0.8"/>
          </svg>
          www.BrinwoodAutoHub.example
        </li>
      </ul>
    </div>
  </section>
</body>
</html>
```